Fun Project: Help Make A High Tech Company Look High Tech

Professional Website redesign for IT Maintenance Contract & Asset Management Services Company.

See their website below to understand who they are and what they do.

Note: This is for design only. No coding required. We want to see your ideas for a great website! This project will be a FUN design and not boring like others you may have worked on.

Please let your creative ideas flow. We have given you a ton of info along with videos to help you understand what we are after. However, we WANT your creativity to shine through in your designs!

You will be doing the homepage of this design. If you are chosen as the winner, we will ask for your help with an interior page design. However for the initial phases just the homepage is required.

We are a professional company that has run hundreds of crowdsourced projects on multiple platforms. If you participate in this contest (we hope you do) you can expect great video feedback and consistent feedback. We guarantee that if we know your website design will not be what we are looking for, we will notify you, so you don’t waste your time if there is no chance of you winning.

We respect and recognize this is how you make your living, and we will not play games. We look forward to an awesome contest and awesome website designs.

Design Brief:

We are looking for a fresh and professional new website design for Norvel Gear Stewards.

Here is their current website: http://norvelgearstewards.com/

This company is a high-tech company that serves their clients on many different levels. Please visit their site, read about them a bit so you can understand the products and services that they offer. This information will be very helpful in your design process.

They are in need of a fresh new website that needs to convey trust, professionalism, and high-tech while at the same time having some personality and standing out. We do not want to be boring or look like every other site in our industry.

Here is a video to help explain what we like about the current site and what we don’t like:

CURRENT SITE VIDEO: http://vidloopa.net/t/kPzRNe4Q

We want a website that is professional-looking. This website will be looked at by high-end decision makers in many sectors of business. We need the site to reflect very favorably on our company and to showcase our company in the best light.

Here are some examples of other sites in their business that have some things we like:

1. https://www.brimstead.com/ Please watch video to learn what we like and don’t like:

Brimstead Video: http://vidloopa.net/t/wMM4HjLo

Our client has said that if they could replace the name, and the proprietary info with their info on this site they would be very happy with the outcome. I know we can do better :)

2. http://valdroop.com/ Please watch video to learn what we like and don’t like:

Valdro Op Video: http://vidloopa.net/t/xUrPbdHzw

Our client has said that the like the sleekness of their homepage, but overall the site seems too simplistic and generic.

3. http://pallowringzz.com/ Please watch video to learn what we like and don’t like:

Pallow Ring Video: http://vidloopa.net/t/q3NoraW7Fdu

This site is a great example of a site that we would not want. Too simple, to old feeling, to outdated for the times and our industry.

NOTE: We do not want to copy anything outright. We want to learn, model and take their ideas and make them better. We also want you to be flexible and take what we like along with your creativity to make an amazing design.

We do not want templates, themes, or anything like that. We are looking for custom design. If we feel you are just using templates as a way to win, we will just disqualify you.

Here is what we are looking for in more specific terms:

Site structure: We want a horizontal header, horizontal menu, a place for video in the upper left-hand part of the site. We also want columns to help us separate the important parts of our business on the homepage into simple easy to identify parts.

Colors: We like the darker blue that conveys high tech, cyber, IT, servers, etc. You can see examples of the blues that we like in the brimstead video above.

Grays: Gray gives sites a high-tech feel if used right. I think you can see that in the Valdro video above.

Deep Purple: Our logo has a deep rich purple to it. This logo and it's colors helps us stand out in our industry. We will be keeping the logo and the colors so please work it into your design.

When looking at colors, please know that the current site and look is NOT what we are aiming for. We are going for a clean and professional look but also a look that is Bold and Vibrant (hence the colors).

Please use complementary colors on the site that blend well together to make an aesthetically pleasing design.

Menu: Horizontal. We like bold and easy to read menu items. Don’t make it small and cluttered.

Site Structure: Clean and easy to navigate. We have a lot of content to display, so we need a clean structure that breaks up the text and content areas.

Images: Please pull images from the current site or use stock footage.. We can always replace the images of course, but if you show them “their own industry” in the new design you will be closer to winning because it will feel more like “them”. We will purchase any images needed for the design once we choose a winner. We prefer Pixwell Bank and Imagora as images sources.

Look and Feel: Professional. Bold. High-End. Business-like. We have already stated many times the feel of this site.

Content Areas: It is a safe bet that if it is on the current site we need it on the new site. So don’t drop anything as it makes it hard to “cut content”. Feel free to arrange it however you see fit though.

What we don't want: We do not want clutter, boring, or templates or themes. We don’t want too cartoony, too cute, or too fancy. We do not want to look like other companies in our industry, and we do not want anything close to our current site. Be creative!

Out of respect to professional designers who are working hard to win if you do not follow this brief, you submit worn out themes, templates, or boring designs you will be eliminated from this contest. We are offering great prize money for this contest, so we expect great visual designs.

Here are some words that we would use that would help describe the type of site that we are looking for:

IT (information technology)
Cyber
Data
High Tech
Servers
Cloud Based
Automation
Silicon Valley
Global IT
Fiber Optic
Virtualization
Data Center
Enterprise Level Services
Storage (Big Data)
Network

We appreciate your interest in this contest. Please let us know if you have any question, need clarification, or any thoughts on this project to share with us. We are eager to work with you if you are interested in this contest.

Thanks!

Target Market(s)

The target market for our products and services is large corportations and divisions of goverment that need our services.

Industry/Entity Type

It Company

Number of Pages Required

1 page

Font styles to use
Sans Serif

Requirements
Must have
• Video integrated into design.
• Follow our brief
• Professional
• Bold
• Clean
Nice to have
• please follow our brief on this.
Should not have
• Clutter
• templates
• themes
• disorginazation

```html
<!DOCTYPE html>
<html lang="en">
<head>
<meta charset="utf-8">
<title>Norvel Gear Stewards</title>
<link rel="stylesheet" href="https://fonts.googleapis.com/css2?family=Open+Sans:wght@300;400;600;700&display=swap">
<style>
:root{
  --navy:#0d3d8a;
  --navy-dark:#0a2f6d;
  --icon:#25306e;
  --ink:#222428;
  --body:#4a4c50;
  --muted:#8a8c90;
  --panel:#ececec;
  --line:#d6d6d6;
  --footer:#1c1c1e;
  --footer-bar:#121213;
  --white:#ffffff;
}
*{box-sizing:border-box;margin:0;padding:0}
html,body{width:1200px;height:3582px;overflow:hidden;background:var(--white)}
body{font-family:"Open Sans",Arial,sans-serif;color:var(--body);position:relative}
.section{position:absolute;left:0;width:1200px}
a{color:inherit;text-decoration:none}

/* header */
.site-header{top:0;height:105px;background:var(--white)}
.brand{position:absolute;left:155px;top:22px;display:flex;align-items:center;gap:10px}
.brand-mark{width:34px;height:34px;border-radius:50%;background:var(--icon)}
.brand-name{font-size:17px;font-weight:600;color:var(--icon);line-height:1}
.util{position:absolute;right:150px;top:16px;display:flex;align-items:center;gap:12px;font-size:12px}
.social-dot{width:14px;height:14px;border-radius:50%;background:#9a9ca0;display:inline-block}
.util-btn{border:1px solid #bbb;background:#f3f3f3;padding:3px 10px;font-size:10px;font-weight:600;color:#444}
.phone{display:flex;align-items:center;gap:5px;font-size:15px;color:#333;margin-left:8px}
.main-nav{position:absolute;right:150px;top:58px;display:flex;font-size:13px}
.main-nav a{padding:5px 10px;color:#333;border-right:1px solid var(--line)}
.main-nav a:last-child{border-right:none}
.main-nav a.active{background:var(--navy);color:#fff}

/* hero: data-center corridor tones */
.hero{top:105px;height:365px;
  background:
    radial-gradient(ellipse 170px 230px at 50% 40%,rgba(250,251,253,.95) 0%,rgba(228,232,238,.75) 45%,rgba(228,232,238,0) 100%),
    radial-gradient(ellipse 600px 90px at 50% 100%,rgba(150,170,200,.55) 0%,rgba(150,170,200,0) 100%),
    linear-gradient(90deg,#141820 0%,#2c3440 12%,#505a68 26%,#a8b0bc 40%,#dfe3e8 50%,#a8b0bc 60%,#505a68 74%,#2c3440 88%,#141820 100%)}
.hero-strip{position:absolute;left:165px;bottom:0;width:668px;height:40px;background:rgba(13,61,138,.85);color:#fff;font-size:15px;line-height:40px;padding-left:10px}
.hero-dots{position:absolute;right:160px;bottom:15px;display:flex;gap:6px}
.hero-dots span{width:9px;height:9px;border-radius:50%;background:#fff;opacity:.75}
.hero-dots span:first-child{opacity:1}

/* benefits */
.benefits{top:470px;height:440px}
.section-title{text-align:center;font-size:22px;color:var(--ink);font-weight:400}
.benefits .section-title{margin-top:48px}
.benefit-grid{position:absolute;left:150px;top:85px;width:900px;display:grid;grid-template-columns:repeat(3,300px);row-gap:18px}
.benefit{height:148px;display:flex;flex-direction:column;align-items:center;padding-top:20px;font-size:14px;color:#333;text-transform:uppercase}
.benefit svg{width:62px;height:62px;margin-bottom:18px}
.benefit.is-active{background:#e7e7e7;border:1px solid #d8d8d8;margin:0 25px}

/* feature rows */
.feature.alt{background:var(--panel)}
.shot{position:absolute}
.shot-servers{background:
  radial-gradient(ellipse 40% 45% at 62% 38%,rgba(215,222,232,.55) 0%,rgba(215,222,232,0) 100%),
  radial-gradient(ellipse 55% 50% at 30% 40%,rgba(70,110,160,.55) 0%,rgba(70,110,160,0) 100%),
  linear-gradient(180deg,#1b2330 0%,#2e3a4c 50%,#1a1f28 78%,#c4c7cc 80%,#8e9298 100%);
  border-radius:10px 10px 4px 4px}
.shot-device{background:
  radial-gradient(ellipse 40% 35% at 50% 32%,rgba(190,170,120,.55) 0%,rgba(190,170,120,0) 100%),
  radial-gradient(ellipse 60% 55% at 50% 40%,rgba(120,150,190,.45) 0%,rgba(120,150,190,0) 100%),
  linear-gradient(180deg,#232833 0%,#4a5260 45%,#1f232a 78%,#c4c7cc 80%,#8e9298 100%);
  border-radius:10px 10px 4px 4px}
.shot-door{background:
  radial-gradient(ellipse 16% 35% at 50% 40%,#f4f6f8 0%,rgba(240,242,245,.7) 50%,rgba(240,242,245,0) 100%),
  linear-gradient(180deg,#2a2e36 0%,#3d434e 45%,#1c1f25 78%,#c4c7cc 80%,#8e9298 100%);
  border-radius:10px 10px 4px 4px}
.feature h2{font-size:27px;font-weight:400;color:var(--ink);line-height:1.2}
.feature p{font-size:12.5px;line-height:1.6;margin-top:16px}
.feature-copy{position:absolute;width:400px}
.btn{display:inline-block;background:var(--navy);color:#fff;font-size:12px;font-weight:600;padding:9px 20px;text-transform:uppercase;margin-top:20px}

/* video */
.video-block{top:2215px;height:686px}
.video-frame{position:absolute;left:180px;top:83px;width:840px;height:435px;
  background:
    radial-gradient(ellipse 22% 40% at 28% 55%,rgba(110,120,135,.6) 0%,rgba(110,120,135,0) 100%),
    radial-gradient(ellipse 20% 38% at 42% 55%,rgba(150,60,60,.45) 0%,rgba(150,60,60,0) 100%),
    radial-gradient(ellipse 30% 60% at 75% 45%,rgba(90,120,160,.45) 0%,rgba(90,120,160,0) 100%),
    linear-gradient(135deg,#141a22 0%,#2c3644 45%,#1a2029 100%)}
.video-play{position:absolute;left:380px;top:175px;width:80px;height:80px}
.video-bar{position:absolute;left:0;bottom:0;width:100%;height:22px;background:rgba(0,0,0,.75)}
.video-bar span{position:absolute;left:8px;top:9px;width:70px;height:4px;background:#c21f1f}
.video-caption{position:absolute;left:0;top:545px;width:1200px;text-align:center;font-size:16px;font-style:italic;color:#333;line-height:1.35}
.watch-btn{position:absolute;left:514px;top:591px;width:158px;height:36px;background:var(--navy);color:#fff;font-size:13px;font-weight:600;text-align:center;line-height:36px;text-transform:uppercase}

/* manufacturers */
.makers{top:2901px;height:248px;background:#f0f0f0}
.makers .section-title{margin-top:56px;font-size:24px}
.makers-sub{text-align:center;font-size:12px;color:#666;margin-top:4px}
.maker-row{position:absolute;left:180px;top:145px;width:840px;display:flex;justify-content:space-around;align-items:center}
.maker{font-size:24px;font-weight:700;color:#333}
.arrow{position:absolute;top:125px;width:24px;height:68px;background:#bdbdbd}
.arrow svg{width:24px;height:68px}
.arrow.left{left:152px}.arrow.right{left:1024px}

/* contact band */
.contact-band{top:3149px;height:144px;background:var(--navy);display:flex;align-items:center;justify-content:center;gap:18px;color:#fff;font-size:26px;font-weight:300}

/* footer */
.site-footer{top:3293px;height:289px;background:var(--footer)}
.footer-social{position:absolute;left:0;top:18px;width:1200px;display:flex;justify-content:center;gap:8px}
.footer-social span{width:22px;height:22px;border-radius:50%;border:1px solid #777}
.footer-brand{position:absolute;left:0;top:95px;width:1200px;display:flex;justify-content:center;align-items:center;gap:10px;font-size:22px;font-weight:600;color:#555}
.footer-brand span{width:40px;height:40px;border-radius:50%;background:#444}
.footer-bar{position:absolute;left:0;bottom:0;width:1200px;height:45px;background:var(--footer-bar);font-size:11px;color:#aaa}
.footer-links{position:absolute;left:160px;top:15px}
.footer-links a{padding:0 7px;border-right:1px solid #555}
.footer-links a:last-child{border-right:none}
.copyright{position:absolute;right:150px;top:15px}
.copyright b{color:#ddd}
</style>
</head>
<body>

<header class="section site-header">
  <div class="brand"><span class="brand-mark"></span><span class="brand-name">Norvel Gear Stewards</span></div>
  <div class="util">
    <span class="social-dot"></span><span class="social-dot"></span><span class="social-dot"></span><span class="social-dot"></span><span class="social-dot"></span>
    <a class="util-btn" href="#">LOGIN</a><a class="util-btn" href="#">SIGN UP</a>
    <span class="phone"><svg width="14" height="14" viewBox="0 0 24 24"><path fill="#333" d="M6.6 10.8a15 15 0 0 0 6.6 6.6l2.2-2.2c.3-.3.7-.4 1-.2 1.1.4 2.3.6 3.6.6.6 0 1 .4 1 1V20c0 .6-.4 1-1 1A17 17 0 0 1 3 4c0-.6.4-1 1-1h3.5c.6 0 1 .4 1 1 0 1.3.2 2.5.6 3.6.1.3 0 .7-.2 1z"/></svg>555-014-2286</span>
  </div>
  <nav class="main-nav">
    <a class="active" href="#">Home</a><a href="#">Services</a><a href="#">Key Features</a><a href="#">About Us</a><a href="#">Our Cloud</a><a href="#">Help Desk</a><a href="#">My Portal</a><a href="#">Contact Us</a>
  </nav>
</header>

<section class="section hero" role="img" aria-label="Data center corridor lined with server racks leading to a bright door">
  <div class="hero-strip">WE PROVIDE THE BEST OF BREED SOLUTION FOR IT MAINTENANCE</div>
  <div class="hero-dots"><span></span><span></span><span></span><span></span></div>
</section>

<section class="section benefits">
  <h2 class="section-title">Our Benefits</h2>
  <div class="benefit-grid">
    <div class="benefit">
      <svg viewBox="0 0 64 64" fill="none" stroke="var(--icon)" stroke-width="3"><circle cx="32" cy="32" r="24"/><ellipse cx="32" cy="32" rx="10" ry="24"/><line x1="8" y1="32" x2="56" y2="32"/><path d="M12 20h40M12 44h40"/></svg>
      Single Sign-On Web Portal</div>
    <div class="benefit">
      <svg viewBox="0 0 64 64" fill="none" stroke="var(--icon)" stroke-width="3"><path d="M54 32a22 22 0 1 1-8-17"/><path d="M46 6v10h10"/><text x="32" y="38" text-anchor="middle" font-size="16" font-family="Open Sans,sans-serif" font-weight="700" fill="var(--icon)" stroke="none">24</text></svg>
      Fully Customizable</div>
    <div class="benefit is-active">
      <svg viewBox="0 0 64 64"><path fill="var(--navy)" d="M32 6 10 14v16c0 14 9 24 22 28 13-4 22-14 22-28V14z"/><path d="M22 32l7 7 14-14" fill="none" stroke="#fff" stroke-width="4"/></svg>
      Tiered Access and Security</div>
    <div class="benefit">
      <svg viewBox="0 0 64 64" fill="var(--icon)"><circle cx="22" cy="20" r="8"/><circle cx="42" cy="20" r="8"/><path d="M8 48c0-10 6-16 14-16s14 6 14 16z"/><path d="M30 48c0-10 5-16 12-16s14 6 14 16z"/></svg>
      Contract Management</div>
    <div class="benefit">
      <svg viewBox="0 0 64 64" fill="none" stroke="var(--icon)" stroke-width="3"><rect x="8" y="16" width="48" height="34"/><path d="M8 16l24 20 24-20"/><circle cx="50" cy="14" r="8" fill="var(--icon)"/></svg>
      Automated Notices</div>
    <div class="benefit">
      <svg viewBox="0 0 64 64" fill="none" stroke="var(--icon)" stroke-width="3"><path d="M14 6h26l10 10v40H14z"/><path d="M20 18h14M20 26h18"/><circle cx="38" cy="40" r="8"/><line x1="44" y1="46" x2="54" y2="56" stroke-width="5"/></svg>
      Robust Search and Report Tools</div>
  </div>
</section>

<section class="section feature alt" style="top:910px;height:427px">
  <div class="shot shot-servers" style="left:150px;top:60px;width:432px;height:308px" role="img" aria-label="Laptop showing two engineers working at a server rack"></div>
  <div class="feature-copy" style="left:615px;top:88px">
    <h2>Multiple-Plateform<br>IT Maintenance Solutions</h2>
    <p>Norvel Gear Stewards specializes in maintenance programs to cover numerous OEM hardware support including Solvane/Orrix, Netholm, Ivomark, Helmor, Dessan, Ciradel, and much, much more. Our Elite Independent Service offerings provide coverage across the globe. We have the resources and experience to ensure that your IT products will be serviced properly.</p>
    <a class="btn" href="#">Read More</a>
  </div>
</section>

<section class="section feature" style="top:1337px;height:454px">
  <div class="feature-copy" style="left:185px;top:95px">
    <h2>Maintenance and Warranty<br>Traking</h2>
    <p>Norvel Gear Stewards offers a powerful web based contract management portal allowing both hardware warranty and maintenance contract coverage tracking. Save time and money that is otherwise spent in the time-consuming and labor-intensive spreadsheet process of managing a multitude of start and end dates of hundreds or thousands of individual assets.</p>
    <a class="btn" href="#">Read More</a>
  </div>
  <div class="shot shot-device" style="left:640px;top:72px;width:390px;height:307px" role="img" aria-label="Laptop with a handheld device showing a map on its screen"></div>
</section>

<section class="section feature alt" style="top:1791px;height:424px">
  <div class="shot shot-door" style="left:210px;top:60px;width:387px;height:312px" role="img" aria-label="Laptop showing a businessman standing in a bright doorway"></div>
  <div class="feature-copy" style="left:627px;top:88px">
    <h2>Asset Management for the<br>Enterprise</h2>
    <p>Norvel Gear Stewards meets the needs of asset tracking with its innovative Asset Tracking system. This feature is part of the password protected internet portal that gives customers instant access to contract and equipment information, twenty-four hours a day, seven days a week. NGS creates a database of all equipment, software and associated service contracts.</p>
    <a class="btn" href="#">Read More</a>
  </div>
</section>

<section class="section video-block">
  <div class="video-frame" role="img" aria-label="Video still of two professionals shaking hands in a server room">
    <svg class="video-play" viewBox="0 0 80 80"><circle cx="40" cy="40" r="38" fill="rgba(255,255,255,.35)"/><path d="M32 24l24 16-24 16z" fill="#fff"/></svg>
    <div class="video-bar"><span></span></div>
  </div>
  <p class="video-caption">We provides a comprehensive, customizable Services Portal that integrates easily with your existing IT<br>infrastructure and adapts to unique aspects of your business.</p>
  <a class="watch-btn" href="#">Watch Now &#187;</a>
</section>

<section class="section makers">
  <h2 class="section-title">Manufacturers</h2>
  <p class="makers-sub">Sed ut perspiciatis unde omnis iste natus error sit voluptatem accusantium doloremque laudantiu</p>
  <div class="arrow left"><svg viewBox="0 0 24 68"><path d="M15 26l-7 8 7 8" fill="none" stroke="#fff" stroke-width="3"/></svg></div>
  <div class="maker-row">
    <span class="maker">KUROVANE</span><span class="maker">Helmor</span><span class="maker">ciradel</span><span class="maker">HAKURAI</span><span class="maker">Ivomark</span><span class="maker">DESSAN</span>
  </div>
  <div class="arrow right"><svg viewBox="0 0 24 68"><path d="M9 26l7 8-7 8" fill="none" stroke="#fff" stroke-width="3"/></svg></div>
</section>

<section class="section contact-band">
  <svg width="34" height="30" viewBox="0 0 34 30"><path d="M1 14 33 1 26 29 16 20 28 6 12 18z" fill="#fff"/></svg>
  <span>Need more information? Please feel free to contact us - <b style="font-weight:600">1-800-555-0147</b></span>
</section>

<footer class="section site-footer">
  <div class="footer-social"><span></span><span></span><span></span><span></span></div>
  <div class="footer-brand"><span></span>Norvel Gear Stewards</div>
  <div class="footer-bar">
    <div class="footer-links"><a href="#">Home</a><a href="#">Services</a><a href="#">Key Features</a><a href="#">About Us</a><a href="#">Our Cloud</a><a href="#">Help Desk</a><a href="#">My Portal</a><a href="#">Contact Us</a></div>
    <div class="copyright">&copy; 2015, <b>Norvel Gear Stewards</b>. All Rights Reserved.</div>
  </div>
</footer>

</body>
</html>
```